Full color cover for Chamber's Membership Menu

I need a cover, 8 1/2" x 11" for our Chamber of Commerce Membership Menu. Is should have our logo and the words, Membership Menu on it. That's all that is necessary but it can include one or more of the other photos (maybe a college?) that I added, though they are not required. Our logo colors should be used: 37-170-226, 58-181-74, 40-56-144, 247-148-29, 189-190-192.

Target Market(s)

Business owners and managers

Industry/Entity Type

Business Development

Font styles to use
Serif

Colors
0054AA
0677BA
7BADD7
CADEEF
E8F1F8
00AB8E
00BBA5
67D7C9
C6EFE9
E9F9F6
F0912C
F2A743
F7CA91
FBE8D2
FDF5EE

Requirements
Must have
• Our logo and the words Membership Menu
Nice to have
• An attractive business-like feel. It can be very simple.

```html
<!DOCTYPE html>
<html lang="en">
<head>
<meta charset="utf-8">
<title>Membership Menu Cover</title>
<link href="https://fonts.googleapis.com/css2?family=Roboto:wght@400;700;900&display=swap" rel="stylesheet">
<style>
  :root {
    --navy: #283890;
    --orange: #f7941d;
    --sky: #25aae2;
    --green: #3ab54a;
    --silver: #bdbec0;
    --peach: #fbe8d2;
    --peach-soft: #fdf5ee;
    --line-blue: #cadeef;
    --ink: #222222;
    --backdrop: #d9dadc;
  }
  html, body {
    margin: 0;
    padding: 0;
    width: 1000px;
    height: 1200px;
    overflow: hidden;
    background: var(--backdrop);
  }
  .cover {
    position: absolute;
    left: 75px;
    top: 50px;
    width: 850px;
    height: 1100px;
    background: #ffffff;
  }
  .cover svg {
    display: block;
    width: 850px;
    height: 1100px;
  }
  .org-name {
    font-family: "Roboto", Arial, sans-serif;
    font-weight: 700;
    fill: var(--navy);
  }
  .org-sub {
    font-family: "Roboto", Arial, sans-serif;
    font-weight: 400;
    fill: var(--navy);
    letter-spacing: 2.2px;
  }
  .title {
    font-family: "Roboto", Arial, sans-serif;
    font-weight: 900;
    fill: var(--navy);
  }
  .contact {
    font-family: "Roboto", Arial, sans-serif;
    font-weight: 400;
    font-size: 12.5px;
    fill: var(--ink);
  }
</style>
</head>
<body>
<main class="cover">
  <svg viewBox="0 0 698 903" xmlns="http://www.w3.org/2000/svg">
    <defs>
      <linearGradient id="peach-band" x1="0" y1="0" x2="1" y2="1">
        <stop offset="0" stop-color="var(--peach)" stop-opacity="0"/>
        <stop offset="0.5" stop-color="var(--peach)"/>
        <stop offset="1" stop-color="var(--peach-soft)" stop-opacity="0"/>
      </linearGradient>
      <linearGradient id="panel-fade" x1="0" y1="0" x2="1" y2="1">
        <stop offset="0" stop-color="var(--peach)"/>
        <stop offset="1" stop-color="#ffffff"/>
      </linearGradient>
      <linearGradient id="green-fill" x1="0" y1="0" x2="1" y2="1">
        <stop offset="0" stop-color="#33b44a"/>
        <stop offset="1" stop-color="#5cc15a"/>
      </linearGradient>
      <linearGradient id="photo-ribbon" x1="0" y1="0" x2="0" y2="1">
        <stop offset="0" stop-color="#9a8d86"/>
        <stop offset="1" stop-color="#3f3b44"/>
      </linearGradient>
      <linearGradient id="photo-staff" x1="0" y1="0" x2="0" y2="1">
        <stop offset="0" stop-color="#7a5a44"/>
        <stop offset="1" stop-color="#2b2523"/>
      </linearGradient>
      <linearGradient id="photo-mixer" x1="0" y1="0" x2="0" y2="1">
        <stop offset="0" stop-color="#6b5a52"/>
        <stop offset="1" stop-color="#35303a"/>
      </linearGradient>
      <linearGradient id="photo-opening" x1="0" y1="0" x2="0" y2="1">
        <stop offset="0" stop-color="#a9c6a8"/>
        <stop offset="1" stop-color="#4a5270"/>
      </linearGradient>
    </defs>

    <!-- background bands and fine lines -->
    <g class="backdrop-decor">
      <polygon points="0,120 120,0 260,0 0,300" fill="url(#peach-band)" opacity="0.8"/>
      <polygon points="560,0 698,0 698,220" fill="url(#peach-band)" opacity="0.7"/>
      <polygon points="380,903 560,700 698,700 698,760 540,903" fill="url(#peach-band)" opacity="0.7"/>
      <g fill="none" stroke="var(--line-blue)" stroke-width="0.7">
        <path d="M0,260 C80,140 200,60 330,0"/>
        <path d="M0,272 C84,150 206,66 342,0"/>
        <path d="M0,284 C88,160 212,72 354,0"/>
        <path d="M0,296 C92,170 218,78 366,0"/>
        <path d="M0,860 C160,800 360,820 520,780"/>
        <path d="M0,872 C160,812 360,832 520,792"/>
        <path d="M0,884 C160,824 360,844 520,804"/>
        <path d="M0,896 C160,836 360,856 520,816"/>
      </g>
    </g>

    <!-- identity -->
    <g class="brand">
      <circle cx="534" cy="86" r="32" fill="var(--sky)"/>
      <text class="org-name" x="656" y="158" text-anchor="end" font-size="23">HARBOR COUNTY CHAMBER</text>
      <text class="org-sub" x="656" y="172" text-anchor="end" font-size="12">OF COMMERCE &amp; TOURISM</text>
    </g>

    <text class="title" x="655" y="254" text-anchor="end" font-size="59" textLength="508" lengthAdjust="spacingAndGlyphs">MEMBERSHIP MENU</text>

    <!-- tile grid -->
    <g class="tiles">
      <rect x="165" y="287" width="176" height="175" rx="14" fill="var(--orange)"/>
      <rect x="146" y="273" width="176" height="176" rx="14" fill="none" stroke="var(--silver)" stroke-width="1.6"/>

      <path role="img" aria-label="Photo: members cutting a ribbon at a business grand opening" d="M369,287 H698 V462 H369 A14,14 0 0 1 355,448 V301 A14,14 0 0 1 369,287 Z" fill="url(#photo-ribbon)"/>

      <path d="M0,475 H137 A14,14 0 0 1 151,489 V636 A14,14 0 0 1 137,650 H0 Z" fill="var(--sky)"/>

      <rect role="img" aria-label="Photo: restaurant staff in aprons standing together" x="165" y="475" width="176" height="175" rx="14" fill="url(#photo-staff)"/>
      <rect role="img" aria-label="Photo: business owners at a networking event" x="355" y="475" width="176" height="175" rx="14" fill="url(#photo-mixer)"/>

      <path d="M698,475 H560 A14,14 0 0 0 546,489 V636 A14,14 0 0 0 560,650 H698 Z" fill="url(#panel-fade)" stroke="var(--silver)" stroke-width="1.6"/>

      <rect role="img" aria-label="Photo: crowd celebrating a ribbon cutting inside a restaurant" x="355" y="664" width="176" height="175" rx="14" fill="url(#photo-opening)"/>

      <path d="M698,664 H557 A14,14 0 0 0 543,678 V825 A14,14 0 0 0 557,839 H698 Z" fill="url(#green-fill)"/>
    </g>

    <!-- contact block -->
    <g class="contact-block">
      <rect x="31" y="736" width="21" height="21" rx="3" fill="var(--orange)"/>
      <rect x="67" y="736" width="21" height="21" rx="3" fill="var(--orange)"/>
      <rect x="103" y="736" width="21" height="21" rx="3" fill="var(--orange)"/>
      <rect x="31" y="769" width="3" height="68" fill="var(--orange)"/>
      <text class="contact" x="45" y="778">555-014-2290</text>
      <text class="contact" x="45" y="798">418 North Elm Street, Riverton, NC 28000</text>
      <text class="contact" x="45" y="818">info@harborcountychamber.com</text>
      <text class="contact" x="45" y="838">www.harborcountychamber.com</text>
    </g>
  </svg>
</main>
</body>
</html>
```